Website to design and sell sundials: www.gnomonvale.com

We have a website that creates a free paper sundial, we want to migrate from this not profit free website to a website where we will continue offering the free paper sundial model but We will also offer a manufactured sundial and sell it.
In order to understand the project, please visit:
http://www.gnomonvale.com/vertical/sundial.html and
http://www.korvel.net/landing/

The website user journey should be redesigned, including the phases that are,
select language
Show product give info
Creation/edit sundial (could be one or more phases)
View created sundial
Buy sundial.

May some of them could be combined or splitted, what It have more sense.

Number of Pages Required

4 page

Font styles to use
Sans Serif

Requirements
Must have
• A description page user journey offering freemium paper sundial and physical sundial to sell.
• A sundial creation page for "free" paper sundial
• A result page for paper sundial
• A sell page for physical

```html
<!DOCTYPE html>
<html lang="en">
<head>
<meta charset="utf-8">
<title>GnomonVale – Sundials</title>
<link href="https://fonts.googleapis.com/css2?family=Roboto:wght@400;500;700&family=Open+Sans:ital,wght@0,400;0,600;1,600&display=swap" rel="stylesheet">
<style>
:root{
  --red:#d52b27;
  --red-dark:#b82220;
  --yellow:#f7ae3a;
  --dark:#1e1e1e;
  --ink:#333333;
  --muted:#8a8a8a;
  --line:#dddddd;
  --white:#ffffff;
}
*{box-sizing:border-box;margin:0;padding:0}
html,body{width:1200px;height:2582px;overflow:hidden;background:var(--white)}
body{position:relative;font-family:"Roboto",Arial,sans-serif;color:var(--ink)}
.abs{position:absolute}
.bands{position:absolute;left:0;top:0;width:1200px;height:2582px}

/* header */
.logo{left:98px;top:42px;display:flex;align-items:center;gap:12px}
.logo-dot{width:26px;height:26px;border-radius:50%;background:var(--yellow)}
.logo-name{font-weight:700;font-size:27px;color:var(--red)}
.social{left:672px;top:30px;display:flex;align-items:center;gap:10px;font-size:11px;color:#666}
.social i{display:block;width:27px;height:27px;border-radius:50%}
.lang{left:993px;top:26px;width:108px;height:30px;border:1px solid var(--line);font-size:11px;color:#555;display:flex;align-items:center;padding-left:10px;gap:8px}
.lang b{width:14px;height:10px;background:#c9d3e6;display:block}
.nav{left:570px;top:72px;display:flex;font-size:11.5px;font-weight:500;color:#333}
.nav a{display:block;padding:6px 20px 22px;color:inherit;text-decoration:none;position:relative}
.nav a.active::after{content:"";position:absolute;left:0;right:0;bottom:0;height:5px;background:var(--yellow)}

/* hero */
.hero-photo{left:0;top:113px;width:1200px;height:600px;
  background:radial-gradient(circle at 720px 220px,#f6b84a 0,#c96d12 90px,#4a2a0e 220px,#150e08 380px,#050505 600px)}
.hero-lead{left:98px;top:214px;font-size:32px;font-weight:400;color:var(--white)}
.hero-title{left:98px;top:266px;font-size:36px;font-weight:700;color:var(--white)}
.hero-text{left:98px;top:320px;width:440px;font-size:15px;line-height:25px;color:#e6e6e6}
.btn{display:flex;align-items:center;justify-content:center;width:134px;height:38px;background:var(--red);color:var(--white);font-size:11px;font-weight:500;border-radius:2px;box-shadow:0 2px 3px rgba(0,0,0,.25)}
.hero-btn{left:98px;top:399px}
.arrow{width:30px;height:30px;border-radius:50%;background:rgba(255,255,255,.15);display:flex;align-items:center;justify-content:center}

/* product info */
.product-photo{left:103px;top:689px;width:198px;height:198px;border-radius:50%;border:5px solid var(--white);
  background:linear-gradient(135deg,#3f5a2a,#7c8f5c 45%,#d9dde0 55%,#a8b0b6)}
.info-title{left:341px;top:696px;font-size:23px;font-weight:500;color:var(--white)}
.info-text{left:341px;top:733px;width:762px;font-family:"Open Sans",Arial,sans-serif;font-size:12.4px;line-height:19.5px;color:var(--white)}
.info-btn{left:341px;top:842px}

/* sections */
.sec-title{left:0;width:1200px;text-align:center;font-size:24px;font-weight:500;color:#333}
.sec-text{left:220px;width:760px;text-align:center;font-size:12.5px;line-height:22px;color:var(--muted)}

.card{left:98px;width:1003px;height:216px;border:1px solid var(--line);background:var(--white)}
.card-photo{top:5px;width:318px;height:205px}
.card-title{font-size:13px;font-weight:700;color:#333}
.card-text{width:585px;font-size:12px;line-height:26px;color:#777}
.photo-ns{left:6px;background:linear-gradient(90deg,#6c7f93 0,#6c7f93 28%,#a0503a 28%,#b5634a 100%)}
.photo-ew{left:679px;background:linear-gradient(90deg,#2b2e2c 0,#2b2e2c 18%,#9fb2c6 18%,#d7c7ad 70%,#6e5842)}

/* create */
.create-title{color:var(--white)}
.create-text{color:#f4d0cf}
.create-sheet{left:98px;top:1750px;width:279px;height:223px;background:linear-gradient(135deg,#f6f6f6,#e8e8ee)}
.steps{left:420px;top:1748px;width:700px}
.step{margin-bottom:26px}
.step-head{display:flex;align-items:center;gap:10px;font-size:13px;font-weight:500;color:var(--white)}
.step-head svg{flex:none}
.step-text{margin-top:6px;font-family:"Open Sans",Arial,sans-serif;font-style:italic;font-weight:600;font-size:10.8px;color:var(--white)}

/* buy */
.shop{left:98px;top:2162px;width:1004px;display:flex;justify-content:space-between}
.item{width:235px;text-align:center}
.item-photo{width:235px;height:178px;border:3px solid #eee}
.item-name{margin-top:22px;font-size:13px;font-weight:700;color:#333}
.item-link{margin-top:6px;font-size:10.5px;font-weight:500;color:var(--red);text-decoration:underline}
.p1{background:linear-gradient(180deg,#8e6f7d,#6d8b53 45%,#7c7870)}
.p2{background:radial-gradient(circle at 50% 60%,#c6b9a8,#8b7f72 70%)}
.p3{background:linear-gradient(180deg,#b6c7d8,#5c7d4a 45%,#c2b7a8 60%,#9f8d7a)}
.p4{background:linear-gradient(180deg,#5b6fa8,#e2e3df 30%,#cfd0cb)}

/* footer */
.foot-head{top:2478px;font-size:12px;font-weight:700;color:var(--white)}
.foot-text{font-size:11px;line-height:24px;color:#9a9a9a;white-space:nowrap}
.foot-item{display:flex;gap:12px;align-items:flex-start}
</style>
</head>
<body>

<div class="abs hero-photo" role="img" aria-label="Photo of open hands holding a glowing clock face on a dark background"></div>

<svg class="bands" viewBox="0 0 1200 2582" aria-hidden="true">
  <path d="M0 548 Q380 720 1200 530 L1200 720 L0 720 Z" fill="var(--red)"/>
  <path d="M0 590 Q420 735 1200 568 L1200 944 Q600 880 0 904 Z" fill="var(--yellow)"/>
  <path d="M0 1565 Q600 1530 1200 1578 L1200 2023 L0 2023 Z" fill="var(--red)"/>
  <path d="M0 2418 Q600 2440 1200 2408 L1200 2582 L0 2582 Z" fill="var(--dark)"/>
</svg>

<!-- header -->
<div class="abs logo"><span class="logo-dot"></span><span class="logo-name">GnomonVale</span></div>
<div class="abs social">Connect with our social network :
  <i style="background:#3b5a9a"></i><i style="background:#3fa9e0"></i><i style="background:#f2a033"></i><i style="background:#2a7d8c"></i>
</div>
<div class="abs lang"><b></b>Language</div>
<nav class="abs nav">
  <a class="active" href="#">HOME</a><a href="#">ABOUT US</a><a href="#">SUNDIAL</a><a href="#">OUR PRODUCT</a><a href="#">BLOG</a><a href="#">CONTACT US</a>
</nav>

<!-- hero -->
<div class="abs hero-lead">Gives you your</div>
<div class="abs hero-title">COUNTRY'S OFFICIAL TIME</div>
<p class="abs hero-text">Sed ut perspiciatis unde omnis iste natus error sit voluptatem accusantium doloremque laudantium, totam...</p>
<div class="abs btn hero-btn">READ MORE INFO</div>
<div class="abs arrow" style="left:44px;top:313px"><svg width="12" height="12" viewBox="0 0 12 12"><path d="M8 1 L3 6 L8 11" fill="none" stroke="#fff" stroke-width="2"/></svg></div>
<div class="abs arrow" style="left:1125px;top:313px"><svg width="12" height="12" viewBox="0 0 12 12"><path d="M4 1 L9 6 L4 11" fill="none" stroke="#fff" stroke-width="2"/></svg></div>

<!-- product info -->
<div class="abs product-photo" role="img" aria-label="Photo of a white paper sundial mounted on a hedge"></div>
<div class="abs info-title">PRODUCT INFORMATION</div>
<p class="abs info-text">Sundials are instruments that tell you the time with the shadow of the sun. To design a sundial you need to know exactly where you are going to put it. I.e. you need to know the longitude, the latitude and the orientation of the wall with respect to North. have designed this page and integrated an interactive map. It helps you to easily find all the parameters needed and finally produces a printable page with a cut-out paper sundial, that can be cut and folded to give you a vertical sundial...</p>
<div class="abs btn info-btn">READ MORE INFO</div>

<!-- how it works -->
<h2 class="abs sec-title" style="top:976px">HOW IT WORKS</h2>
<p class="abs sec-text" style="top:1010px">Sed ut perspiciatis unde omnis iste natus error sit voluptatem accusantium doloremque laudantium, totam rem aperiam, eaque ipsa quae ab illo inventore veritatis et quasi architecto beatae vitae dicta sunt explicabo.</p>

<div class="abs card" style="top:1081px">
  <div class="abs card-photo photo-ns" role="img" aria-label="Photo of a paper sundial fixed on a brick wall"></div>
  <div class="abs card-title" style="left:379px;top:28px">NORTH / SOUTH SUNDIAL ZONE</div>
  <p class="abs card-text" style="left:379px;top:54px">Sed ut perspiciatis unde omnis iste natus error sit voluptatem accusantium doloremque laudantium, totam rem aperiam, eaque ipsa quae ab illo inventore veritatis et quasi architecto beatae vitae dicta sunt Nemo enim ipsam voluptatem quia voluptas sit aspernatur aut odit aut fugit, sed quia consequuntur...</p>
  <div class="abs btn" style="left:379px;top:152px">READ MORE INFO</div>
</div>

<div class="abs card" style="top:1322px">
  <div class="abs card-title" style="left:31px;top:28px">EAST / WEST SUNDIAL ZONE</div>
  <p class="abs card-text" style="left:31px;top:54px">Sed ut perspiciatis unde omnis iste natus error sit voluptatem accusantium doloremque laudantium, totam rem aperiam, eaque ipsa quae ab illo inventore veritatis et quasi architecto beatae vitae dicta sunt Nemo enim ipsam voluptatem quia voluptas sit aspernatur aut odit aut fugit, sed quia consequuntur...</p>
  <div class="abs btn" style="left:31px;top:149px">READ MORE INFO</div>
  <div class="abs card-photo photo-ew" role="img" aria-label="Photo of a paper sundial on a balcony window"></div>
</div>

<!-- create -->
<h2 class="abs sec-title create-title" style="top:1640px">CREATE YOUR SUNDIAL</h2>
<p class="abs sec-text create-text" style="top:1673px">Sed ut perspiciatis unde omnis iste natus error sit voluptatem accusantium doloremque laudantium, totam rem aperiam, eaque ipsa quae ab illo inventore veritatis et quasi architecto beatae vitae dicta sunt explicabo.</p>
<div class="abs create-sheet" role="img" aria-label="Printable paper sundial cut-out template with hour lines"></div>
<div class="abs steps">
  <div class="step"><div class="step-head"><svg width="14" height="14" viewBox="0 0 14 14"><circle cx="7" cy="7" r="7" fill="#fff"/><path d="M5.5 4 L8.5 7 L5.5 10" fill="none" stroke="var(--red)" stroke-width="1.8"/></svg>PRINT THE PDF</div><p class="step-text">Sed ut perspiciatis unde omnis iste natus error sit voluptatem accusantium doloremque laudantium, totam rem aperiam, eaque ipsa quae.</p></div>
  <div class="step"><div class="step-head"><svg width="14" height="14" viewBox="0 0 14 14"><circle cx="7" cy="7" r="7" fill="#fff"/><path d="M5.5 4 L8.5 7 L5.5 10" fill="none" stroke="var(--red)" stroke-width="1.8"/></svg>CUT AND FOLD</div><p class="step-text">Sed ut perspiciatis unde omnis iste natus error sit voluptatem accusantium doloremque laudantium, totam rem aperiam, eaque ipsa quae.</p></div>
  <div class="step"><div class="step-head"><svg width="14" height="14" viewBox="0 0 14 14"><circle cx="7" cy="7" r="7" fill="#fff"/><path d="M5.5 4 L8.5 7 L5.5 10" fill="none" stroke="var(--red)" stroke-width="1.8"/></svg>PUT ON YOUR WALL</div><p class="step-text">Sed ut perspiciatis unde omnis iste natus error sit voluptatem accusantium doloremque laudantium, totam rem aperiam, eaque ipsa quae.</p></div>
  <div class="step"><div class="step-head"><svg width="14" height="14" viewBox="0 0 14 14"><circle cx="7" cy="7" r="7" fill="#fff"/><path d="M5.5 4 L8.5 7 L5.5 10" fill="none" stroke="var(--red)" stroke-width="1.8"/></svg>ENJOY SUNDIAL</div><p class="step-text">Sed ut perspiciatis unde omnis iste natus error sit voluptatem accusantium doloremque laudantium, totam rem aperiam, eaque ipsa quae.</p></div>
</div>

<!-- buy -->
<h2 class="abs sec-title" style="top:2058px">BUY SUNDIAL</h2>
<p class="abs sec-text" style="top:2092px">Sed ut perspiciatis unde omnis iste natus error sit voluptatem accusantium doloremque laudantium, totam rem aperiam, eaque ipsa quae ab illo inventore veritatis et quasi architecto beatae vitae dicta sunt explicabo.</p>
<div class="abs shop">
  <div class="item"><div class="item-photo p1" role="img" aria-label="Photo of a bronze garden sundial among flowers"></div><div class="item-name">CONSECTETUR ADIPISCING</div><div class="item-link">CLICK TO BUY NOW!</div></div>
  <div class="item"><div class="item-photo p2" role="img" aria-label="Photo of a round stone sundial dial with numerals"></div><div class="item-name">CONSECTETUR ADIPISCING</div><div class="item-link">CLICK TO BUY NOW!</div></div>
  <div class="item"><div class="item-photo p3" role="img" aria-label="Photo of an armillary sundial on a stone pedestal"></div><div class="item-name">CONSECTETUR ADIPISCING</div><div class="item-link">CLICK TO BUY NOW!</div></div>
  <div class="item"><div class="item-photo p4" role="img" aria-label="Photo of a painted wall sundial"></div><div class="item-name">CONSECTETUR ADIPISCING</div><div class="item-link">CLICK TO BUY NOW!</div></div>
</div>

<!-- footer -->
<div class="abs foot-head" style="left:98px">COPY RIGHTS</div>
<div class="abs foot-text" style="left:98px;top:2506px">©GNOMONVALE.2016 | ALLRIGHTS RESERVED.<br>TERMS &amp; CONDITIONS</div>
<div class="abs foot-head" style="left:406px">CONTACT</div>
<div class="abs foot-text foot-item" style="left:406px;top:2506px">
  <svg width="22" height="28" viewBox="0 0 22 28"><path d="M11 26 C4 17 2 13 2 10 A9 9 0 0 1 20 10 C20 13 18 17 11 26 Z" fill="none" stroke="#9a9a9a" stroke-width="1.6"/><circle cx="11" cy="10" r="3.2" fill="none" stroke="#9a9a9a" stroke-width="1.6"/></svg>
  <span>17, GNOMONVALE WORKSHOP,<br>ORCHARD LANE, CITY-4021</span>
</div>
<div class="abs foot-text foot-item" style="left:676px;top:2506px">
  <svg width="16" height="28" viewBox="0 0 16 28"><rect x="2" y="2" width="12" height="24" rx="2" fill="none" stroke="#9a9a9a" stroke-width="1.6"/><line x1="6" y1="22" x2="10" y2="22" stroke="#9a9a9a" stroke-width="1.6"/></svg>
  <span>PHONE:(+1 555) 0142-7781</span>
</div>
<div class="abs foot-text foot-item" style="left:899px;top:2506px">
  <svg width="24" height="22" viewBox="0 0 24 22"><rect x="2" y="5" width="20" height="15" fill="none" stroke="#9a9a9a" stroke-width="1.6"/><path d="M2 5 L12 13 L22 5" fill="none" stroke="#9a9a9a" stroke-width="1.6"/><path d="M6 5 L12 1 L18 5" fill="none" stroke="#9a9a9a" stroke-width="1.6"/></svg>
  <span>MAIL:INFO@GNOMONVALE.COM</span>
</div>

</body>
</html>
```